Business Cards for Maple Ridge Insurance
Use uploaded logo
Business Cards for Maple Ridge Insurance - Financial Services
Creative Brief
Professional
Dwight K Marlowe III
Owner / Producer
3821 Fenwick Rd, Biloxi, MS 39520
228.HAMPTON
dwight@mapleridgeagency.example
www.mapleridgeagency.example
Our land lines will be known by Monday afternoon 4/26. Please include phone line areas for: Office: Fax: Direct: Cell: We would like the Direct and Cell on the bottom LEFT and the Office and Fax on the bottom RIGHT
Be creative but put ensure (228) HAMPTON is centered somewhere. Thanks.

```html
<!DOCTYPE html>
<html lang="en">
<head>
<meta charset="utf-8">
<title>Maple Ridge Insurance — Business Cards</title>
<link rel="stylesheet" href="https://fonts.googleapis.com/css2?family=Montserrat:wght@400;500;600;700&display=swap">
<style>
  :root {
    --backdrop: #6b6b6b;
    --card: #ffffff;
    --orange: #f39a1f;
    --blue: #2a87c8;
    --ink: #333a40;
    --muted: #8ea3b3;
  }
  * { margin: 0; padding: 0; box-sizing: border-box; }
  html, body { width: 1200px; height: 871px; overflow: hidden; }
  body {
    background: var(--backdrop);
    font-family: "Montserrat", Arial, sans-serif;
    position: relative;
  }
  .card {
    position: absolute;
    left: 329px;
    width: 552px;
    height: 350px;
    background: var(--card);
    box-shadow: 0 4px 14px rgba(0,0,0,0.25);
  }
  .card--front { top: 68px; }
  .card--back { top: 456px; }

  /* Front */
  .brand {
    position: absolute;
    top: 138px;
    left: 0; right: 0;
    display: flex;
    align-items: center;
    justify-content: center;
    gap: 14px;
  }
  .brand__mark { width: 34px; height: 34px; border-radius: 50%; background: var(--orange); }
  .brand__name { font-size: 34px; font-weight: 600; color: var(--orange); letter-spacing: 0.5px; }
  .website {
    position: absolute;
    top: 283px;
    left: 0; right: 0;
    text-align: center;
    font-size: 18px;
    font-weight: 500;
    letter-spacing: 1.5px;
    color: var(--ink);
  }
  .website__domain { color: var(--blue); }

  /* Back */
  .holder {
    position: absolute;
    top: 18px;
    left: 0; right: 0;
    text-align: center;
  }
  .holder__name { font-size: 22px; font-weight: 600; color: var(--orange); letter-spacing: 2px; }
  .holder__role { margin-top: 6px; font-size: 18px; font-weight: 400; color: var(--muted); letter-spacing: 4px; }
  .vanity {
    position: absolute;
    top: 161px;
    left: 0; right: 0;
    text-align: center;
    font-size: 24px;
    font-weight: 700;
    color: var(--blue);
  }
  .vanity__area { color: var(--orange); }
  .side-line {
    position: absolute;
    top: 50%;
    font-size: 12px;
    color: var(--blue);
    white-space: nowrap;
    letter-spacing: 0.3px;
  }
  .side-line--email { left: 25px; transform: translate(-50%, -50%) rotate(-90deg); }
  .side-line--address { left: 530px; transform: translate(-50%, -50%) rotate(90deg); }
  .emblem {
    position: absolute;
    left: 246px;
    top: 253px;
    width: 60px;
    height: 60px;
    border-radius: 50%;
    background: var(--orange);
  }
  .phones {
    position: absolute;
    top: 282px;
    font-size: 13px;
    line-height: 20px;
    color: var(--blue);
  }
  .phones--left { left: 14px; }
  .phones--right { left: 398px; }
  .phones__label { color: var(--orange); }
</style>
</head>
<body>
  <section class="card card--front">
    <div class="brand">
      <span class="brand__mark"></span>
      <span class="brand__name">Maple Ridge Insurance</span>
    </div>
    <p class="website">www.<span class="website__domain">mapleridgeagency</span>.example</p>
  </section>

  <section class="card card--back">
    <div class="holder">
      <h1 class="holder__name">DWIGHT K MARLOWE III</h1>
      <p class="holder__role">OWNER / PRODUCER</p>
    </div>
    <p class="vanity"><span class="vanity__area">228.</span>HAMPTON</p>
    <p class="side-line side-line--email">dwight@mapleridgeagency.example</p>
    <p class="side-line side-line--address">3821 Fenwick Rd, Biloxi, MS 39520</p>
    <span class="emblem"></span>
    <div class="phones phones--left">
      <p><span class="phones__label">Direct:</span> 228.555.0142</p>
      <p><span class="phones__label">Cell:</span> 228.555.0142</p>
    </div>
    <div class="phones phones--right">
      <p><span class="phones__label">Office:</span> 228.555.0142</p>
      <p><span class="phones__label">Fax:</span> 228.555.0142</p>
    </div>
  </section>
</body>
</html>
```